Professional Website for Brightfold Laundry Company

Brightfold Laundry Company is a family-owned laundry service provider that has been serving Midtown Atlanta for over 45 years. We provide express clothing and linen washing services to residential and commercial clients in Atlanta and surrounding areas.

The final website and logo design should convey professionalism and give the customer a sense of security in having their personal items laundered with us.

Target Market(s)

Commercial Businesses and high net worth personal customers

Industry/Entity Type

Professional Laundry Services

Coding

Coded - Design and coding required

Number of Pages Required

5+ page

Font styles to use
Sans Serif

Colors
0054AA
0677BA
7BADD7
CADEEF
E8F1F8

Requirements
Must have
• I would like to have the following elements on my website: 1. Blog page 2. Contact Us Form 3. Sign up for service (sample attached) 4. Sections outlined in the content copy page 5. Links to social media accounts.
Nice to have
• A great example is https://www.quillmarsh.example/laundry-pick-up-and-delivery/?utm_term=pick%20up%20and%20delivery%20laundry%20service&utm_campaign=*QM%20United%20States%20%7C%20Search%20(Broad%20KWs)&utm_source=zorvik&utm_medium=ppc&hsa_acc=1111111111&hsa_cam=22222222222&hsa_grp=3333333333333333&hsa_ad=&hsa_src=o&hsa_tgt=kwd-44444444444444:loc-100&hsa_kw=pick%20up%20and%20delivery%20laundry%20service&hsa_mt=e&hsa_net=zorvik&hsa_ver=3&msclkid=00000000000000000000000000000000

```html
<!DOCTYPE html>
<html lang="en">
<head>
<meta charset="utf-8">
<title>Brightfold Laundry Company</title>
<link href="https://fonts.googleapis.com/css2?family=Poppins:wght@300;400;500;600;700&display=swap" rel="stylesheet">
<style>
:root{
  --blue-deep:#0054AA;
  --blue:#0677BA;
  --blue-mid:#7BADD7;
  --blue-soft:#CADEEF;
  --blue-pale:#E8F1F8;
  --red:#E0312F;
  --ink:#1f2a36;
  --text:#5a6470;
  --grey:#f3f4f6;
  --footer:#1b1d21;
  --footer-bar:#111316;
  --white:#ffffff;
}
*{box-sizing:border-box;margin:0;padding:0}
html,body{width:1200px;height:4040px;overflow:hidden}
body{font-family:'Poppins',sans-serif;color:var(--text);background:var(--white);font-size:13px;line-height:1.6}
.btn{display:inline-block;background:var(--red);color:var(--white);font-size:12px;font-weight:500;padding:9px 20px;border-radius:3px;text-decoration:none}
.btn-blue{background:var(--blue)}
.section-title{font-size:38px;font-weight:300;color:var(--ink);text-align:center;line-height:1.2}
.section-title strong{font-weight:600;color:var(--blue)}
.rule{width:60px;height:2px;background:var(--blue);margin:12px auto 0}

/* header */
.site-header{height:80px;display:flex;align-items:center;justify-content:space-between;padding:0 80px 0 60px;border-bottom:1px solid #eee}
.brand{font-size:17px;font-weight:600;color:var(--blue-deep);line-height:1.1;width:150px}
.main-nav{display:flex;align-items:center;gap:28px;font-size:12px;color:var(--ink);font-weight:500}
.main-nav .btn{margin-left:6px}

/* hero */
.hero{height:380px;position:relative;display:flex}
.hero-copy{width:600px;padding:48px 0 0 60px}
.hero-copy h1{font-size:30px;font-weight:600;color:var(--blue);line-height:1.2;margin-bottom:18px}
.hero-copy p{font-size:21px;color:var(--ink);line-height:1.45;margin-bottom:36px;max-width:500px}
.hero-photo{position:absolute;right:0;top:0;width:620px;height:380px;
  background:
    radial-gradient(ellipse 40% 55% at 62% 42%,rgba(255,255,255,.85),rgba(255,255,255,0) 70%),
    radial-gradient(ellipse 45% 30% at 55% 88%,rgba(6,119,186,.55),rgba(6,119,186,0) 75%),
    linear-gradient(100deg,#ffffff 0%,#eef2f6 22%,#d5e0ea 50%,#b7cbe0 80%,#9fb9d4 100%)}

/* welcome */
.welcome{height:440px;padding:20px 112px 0}
.welcome-box{background:var(--blue);height:380px;display:flex;align-items:center;padding:0 60px;gap:60px}
.welcome-photo{width:300px;height:300px;border-radius:50%;border:10px solid var(--blue-soft);flex:none;
  background:radial-gradient(circle at 38% 35%,#ffffff 0%,#e4edf5 35%,#a9c4de 70%,#5f8fbf 100%)}
.welcome-copy h2{font-size:36px;font-weight:300;color:var(--white);line-height:1.2;margin-bottom:16px}
.welcome-copy h2 strong{font-weight:600}
.welcome-copy p{color:var(--blue-pale);font-size:12px;margin-bottom:12px}

/* services */
.services{height:600px;padding-top:56px}
.services .lede{max-width:880px;margin:18px auto 36px;text-align:center;font-size:13px}
.service-track{position:relative;width:1000px;margin:0 auto;display:flex;gap:28px}
.arrow-btn{position:absolute;top:70px;width:28px;height:28px;border-radius:50%;background:var(--white);box-shadow:0 1px 4px rgba(0,0,0,.25);display:flex;align-items:center;justify-content:center}
.arrow-btn.prev{left:-14px}.arrow-btn.next{right:-14px}
.service-card{flex:1}
.service-img{height:160px;margin-bottom:14px}
.img-a{background:radial-gradient(circle at 35% 50%,#d9dee3 0%,#9aa6b2 35%,#4f5d6c 100%)}
.img-b{background:linear-gradient(180deg,#eef2f5 0%,#d7e1ea 45%,#8fa9c2 100%)}
.img-c{background:radial-gradient(ellipse at 60% 40%,#c5d6e6 0%,#7e9dbd 55%,#4a6a8e 100%)}
.service-card h3{font-size:14px;font-weight:600;color:var(--ink);margin-bottom:6px}
.service-card p{font-size:11px;line-height:1.55}
.service-card ul{font-size:11px;columns:2;list-style:none}
.service-card li::before{content:"• ";color:var(--blue)}
.services .btn-row{text-align:center;margin-top:40px}

/* why */
.why{height:700px;background:var(--grey);padding-top:58px}
.why-grid{width:1000px;margin:40px auto 0;display:grid;grid-template-columns:repeat(4,1fr);column-gap:40px;row-gap:36px}
.why-item{text-align:center}
.why-icon{width:56px;height:56px;border-radius:50%;background:var(--blue);margin:0 auto 12px;display:flex;align-items:center;justify-content:center}
.why-item h3{font-size:13px;font-weight:600;color:var(--ink);line-height:1.35;margin-bottom:10px;min-height:36px}
.why-item p{font-size:11px;line-height:1.55;margin-bottom:8px}
.read-more{font-size:11px;color:var(--blue);font-weight:500}
.why .btn-row{text-align:center;margin-top:34px}

/* steps */
.steps{height:610px;padding-top:44px;position:relative}
.step{position:absolute;width:480px}
.step h3{font-size:18px;font-weight:600;color:var(--ink);margin-bottom:8px}
.step p{font-size:12px}
.step-num{position:absolute;width:100px;height:100px;border-radius:50%;border:3px solid var(--blue);display:flex;align-items:center;justify-content:center;font-size:44px;font-weight:300;color:var(--blue);background:var(--white)}
.step-num.alt{color:var(--red)}
.step-curve{position:absolute;left:0;top:0}

/* cta */
.cta{height:410px;position:relative;background:linear-gradient(90deg,#2f6fa6 0%,#4b8cc2 45%,#8eb7da 100%)}
.cta-copy{position:absolute;left:170px;top:150px;color:var(--white)}
.cta-copy h2{font-size:40px;font-weight:300;line-height:1.1;margin-bottom:8px}
.cta-copy p{font-size:19px;line-height:1.35;color:var(--blue-pale)}
.cta-copy p strong{color:var(--white);font-weight:600}
.form-card{position:absolute;left:660px;top:30px;width:400px;height:350px;background:var(--white);padding:24px 26px;box-shadow:0 4px 16px rgba(0,0,0,.15)}
.field{border:1px solid #d6dbe1;height:30px;font-size:10px;color:#7b8490;padding:7px 10px;margin-bottom:10px;border-radius:2px}
.field-row{display:flex;gap:10px}.field-row .field{flex:1}
.field.area{height:48px}
.form-card .btn{display:block;width:70px;margin:4px auto 0;text-align:center;padding:7px 0;font-size:11px}

/* faq */
.faq{height:520px;padding-top:44px}
.faq-list{width:600px;margin:30px auto 0}
.faq-item{display:flex;justify-content:space-between;align-items:center;border-bottom:1px solid #e3e6ea;padding:10px 4px;font-size:12px;color:var(--ink);font-weight:500}
.faq-item.open{background:var(--blue);color:var(--white);border:none;padding:10px 12px}
.faq-answer{background:var(--blue-pale);font-size:11px;padding:10px 12px 12px;line-height:1.55;margin-bottom:4px}
.plus{width:16px;height:16px;border-radius:50%;background:var(--red);color:var(--white);font-size:12px;line-height:16px;text-align:center;flex:none}
.faq .btn-row{text-align:center;margin-top:30px}

/* footer */
.site-footer{height:300px;background:var(--footer);color:#c7cbd1;position:relative}
.footer-cols{display:flex;padding:44px 100px 0;gap:60px}
.footer-col h4{color:var(--white);font-size:14px;font-weight:600;margin-bottom:12px}
.footer-col ul{list-style:none;font-size:11px;line-height:1.95}
.footer-col .hl{color:var(--red)}
.contact-line{display:flex;gap:8px;align-items:flex-start;font-size:11px;margin-bottom:8px}
.contact-line.big{font-size:15px;color:var(--white);font-weight:500}
.footer-bar{position:absolute;bottom:0;left:0;right:0;height:44px;background:var(--footer-bar);display:flex;align-items:center;padding:0 100px;gap:40px;font-size:11px}
.footer-bar .spacer{flex:1}
.to-top{position:absolute;right:60px;top:180px;width:28px;height:28px;background:var(--blue);display:flex;align-items:center;justify-content:center}
</style>
</head>
<body>

<header class="site-header">
  <div class="brand">Brightfold Laundry Company</div>
  <nav class="main-nav">
    <span>About Us</span><span>Our Services ▾</span><span>Why Choose Us</span><span>How To Get Started</span><span>FAQ</span><span>Contact Us</span>
    <a class="btn" href="#">Get Started Today</a>
  </nav>
</header>

<section class="hero">
  <div class="hero-copy">
    <h1>Brightfold Laundry Company</h1>
    <p>We provide express clothing and linen washing services to residential and commercial clients in Atlanta and surrounding areas.</p>
    <a class="btn" href="#">Contact Us</a>
  </div>
  <div class="hero-photo" role="img" aria-label="Photo of a laundry worker holding a stack of folded blue and white towels"></div>
</section>

<section class="welcome">
  <div class="welcome-box">
    <div class="welcome-photo" role="img" aria-label="Circular photo of freshly folded white linen"></div>
    <div class="welcome-copy">
      <h2>Welcome to <strong>Brightfold Laundry Company</strong></h2>
      <p>Brightfold Laundry Company is a family-owned laundry service provider that has been serving Midtown Atlanta for over 45 years. We are proud to offer high quality and dependable service to the many residential and business clients who trust us with their personal items every week.</p>
      <p>Whether you have commercial laundry needs, are seeking clothes for your family, or want to keep your weekend free, let us put our professional team to work for you. Our professionals at Brightfold handle every item with care and attention to detail.</p>
      <a class="btn" href="#">Learn More</a>
    </div>
  </div>
</section>

<section class="services">
  <h2 class="section-title">Our Services</h2>
  <div class="rule"></div>
  <p class="lede">Running a small business is not easy and the last thing you need is another tedious action item like doing laundry on your to do list. Whether it is towels, linens or uniforms, outsourcing your laundry needs to Brightfold Laundry Company will allow you to focus on your business. We promise to provide on time and reliable service.</p>
  <div class="service-track">
    <span class="arrow-btn prev"><svg width="10" height="10" viewBox="0 0 10 10"><path d="M7 1 3 5l4 4" fill="none" stroke="#1f2a36" stroke-width="1.6"/></svg></span>
    <article class="service-card">
      <div class="service-img img-a" role="img" aria-label="Photo of industrial washing machines in a commercial laundry"></div>
      <h3>Commercial Services</h3>
      <p>Our state of the art laundry processing center is designed for the efficiency our commercial clients expect. We handle staff garments, table and bed linen in bulk, with careful sorting, pressing and packaging so every order returns fresh and on schedule.</p>
    </article>
    <article class="service-card">
      <div class="service-img img-b" role="img" aria-label="Photo of neatly folded towels on a counter"></div>
      <h3>Light Commercial Services</h3>
      <ul><li>Daycare Centers</li><li>Dog Groomers</li><li>Massage Therapists</li><li>Hair Salons</li><li>Fitness Clubs</li><li>Dentists</li><li>Spas and Studios</li><li>Restaurants</li></ul>
    </article>
    <article class="service-card">
      <div class="service-img img-c" role="img" aria-label="Photo of pressed shirts on hangers"></div>
      <h3>Professional Laundry Services</h3>
      <p>If you want to enjoy the perks of dry cleaning without all the chemicals, we offer a wash, dry and press service for your garments. You can relax knowing that your clothes will be handled with care and returned crisp and ready to wear.</p>
    </article>
    <span class="arrow-btn next"><svg width="10" height="10" viewBox="0 0 10 10"><path d="M3 1l4 4-4 4" fill="none" stroke="#1f2a36" stroke-width="1.6"/></svg></span>
  </div>
  <div class="btn-row"><a class="btn" href="#">View All Services</a></div>
</section>

<section class="why">
  <h2 class="section-title">Why Choose Brightfold Laundry Company</h2>
  <div class="rule"></div>
  <div class="why-grid">
    <div class="why-item"><div class="why-icon"><svg width="26" height="26" viewBox="0 0 26 26"><circle cx="13" cy="13" r="9" fill="none" stroke="#fff" stroke-width="2"/><path d="M13 8v5l4 2" fill="none" stroke="#fff" stroke-width="2"/></svg></div><h3>We Help You Optimize Your Time</h3><p>Laundry is time consuming, especially for multi-tasking entrepreneurs. Brightfold takes a load off your plate so you can get back to what you do best.</p><span class="read-more">Read More »</span></div>
    <div class="why-item"><div class="why-icon"><svg width="26" height="26" viewBox="0 0 26 26"><circle cx="13" cy="9" r="4" fill="#fff"/><path d="M5 21c1-6 15-6 16 0z" fill="#fff"/></svg></div><h3>We Have Knowledgeable, Friendly Team Members</h3><p>Our family owned team has served Midtown for decades. We know the fabrics, the stains and the people, and we treat every order personally.</p><span class="read-more">Read More »</span></div>
    <div class="why-item"><div class="why-icon"><svg width="26" height="26" viewBox="0 0 26 26"><path d="M13 3l2.6 6 6.4.5-4.9 4.2 1.5 6.3L13 16.6 7.4 20l1.5-6.3L4 9.5l6.4-.5z" fill="#fff"/></svg></div><h3>Our Facility is Bright, Clean and Comfortable</h3><p>We keep the inside of our facility well lit, clean and fully sanitized. Each item is processed with strict hygiene standards at every step.</p><span class="read-more">Read More »</span></div>
    <div class="why-item"><div class="why-icon"><svg width="26" height="26" viewBox="0 0 26 26"><rect x="5" y="3" width="16" height="20" rx="2" fill="none" stroke="#fff" stroke-width="2"/><circle cx="13" cy="14" r="5" fill="none" stroke="#fff" stroke-width="2"/></svg></div><h3>We Utilize Modern, Industrial Size Washer and Dryer Equipment</h3><p>Our technologically advanced machines can handle the biggest loads and use less water and energy than home units.</p><span class="read-more">Read More »</span></div>
    <div class="why-item"><div class="why-icon"><svg width="26" height="26" viewBox="0 0 26 26"><rect x="3" y="7" width="20" height="13" rx="2" fill="none" stroke="#fff" stroke-width="2"/><path d="M3 11h20" stroke="#fff" stroke-width="2"/></svg></div><h3>We Provide Payment Options</h3><p>Our payment platform provides you with several choices. You can pay by credit card, invoice or monthly account.</p><span class="read-more">Read More »</span></div>
    <div class="why-item"><div class="why-icon"><svg width="26" height="26" viewBox="0 0 26 26"><path d="M5 13l5 5 11-11" fill="none" stroke="#fff" stroke-width="2.4"/></svg></div><h3>We Provide Customized Business Solutions</h3><p>Schedules set to fit your day, volumes adjusted by season and packaging made for your staff so nothing gets lost.</p><span class="read-more">Read More »</span></div>
    <div class="why-item"><div class="why-icon"><svg width="26" height="26" viewBox="0 0 26 26"><path d="M13 3a7 7 0 0 0-7 7c0 5 7 13 7 13s7-8 7-13a7 7 0 0 0-7-7z" fill="#fff"/><circle cx="13" cy="10" r="2.6" fill="#0677BA"/></svg></div><h3>Convenient Location</h3><p>Located just north of Midtown, Brightfold is easy to reach for quick drop offs and pickups on your way to work.</p><span class="read-more">Read More »</span></div>
  </div>
  <div class="btn-row"><a class="btn" href="#">Get Started Today</a></div>
</section>

<section class="steps">
  <h2 class="section-title">How To <strong>Get Started</strong></h2>
  <div class="rule"></div>
  <svg class="step-curve" width="1200" height="610" viewBox="0 0 1200 610"><path d="M400 200 C600 210 760 240 810 300 M810 390 C720 440 520 450 400 490" fill="none" stroke="#CADEEF" stroke-width="2" stroke-dasharray="6 6"/></svg>
  <div class="step-num" style="left:300px;top:150px">1</div>
  <div class="step" style="left:450px;top:150px"><h3>Sign Up</h3><p>When setting up your customer profile you can detail how you want your laundry processed, hangers for shirts, special folding, etc. You can select your preferred pickup days, detergents and softeners from a list of provided products.</p></div>
  <div class="step" style="left:270px;top:300px"><h3>Fill Out a Customer Profile</h3><p>When setting up your customer profile you can detail how you want your laundry processed, hangers for shirts, special folding, etc. You can select your laundry detergents, bleaches and softeners from a list of provided products.</p></div>
  <div class="step-num alt" style="left:800px;top:295px">2</div>
  <div class="step-num" style="left:300px;top:445px">3</div>
  <div class="step" style="left:450px;top:450px"><h3>Schedule a Pickup</h3><p>Place your clothes in the Brightfold Laundry bag and leave it out on your scheduled pickup day. We will process your clothing as instructed and deliver it back to your doorstep within 24 hours.</p></div>
</section>

<section class="cta" role="img" aria-label="Background photo of a laundry room with stacked baskets, tinted blue">
  <div class="cta-copy">
    <h2>Let's Get Started</h2>
    <p>Complete the form below to <strong>schedule a<br>pickup or delivery.</strong></p>
  </div>
  <form class="form-card">
    <div class="field-row"><div class="field">First Name*</div><div class="field">Last Name*</div></div>
    <div class="field">What service are you interested in?*</div>
    <div class="field">Management Company or Private Owner?*</div>
    <div class="field">Enter Your Email*</div>
    <div class="field-row"><div class="field">Phone Number*</div><div class="field">Zip Code*</div></div>
    <div class="field area">Additional Details/Information</div>
    <span class="btn btn-blue">Submit</span>
  </form>
</section>

<section class="faq">
  <h2 class="section-title">Frequently Asked Questions</h2>
  <div class="rule"></div>
  <div class="faq-list">
    <div class="faq-item">Can I Customize My Service?<span class="plus">+</span></div>
    <div class="faq-item open">Are Laundry Bags Provided?<span class="plus">−</span></div>
    <div class="faq-answer">Yes, every new customer receives two branded laundry bags at no cost. Simply place your items in the bag on your scheduled day and leave it at your door. Additional bags can be added to your order at any time from your customer profile, and replacement bags are always free.</div>
    <div class="faq-item">What is the Turnaround Time?<span class="plus">+</span></div>
    <div class="faq-item">How Do We Pay?<span class="plus">+</span></div>
    <div class="faq-item">Do you have a referral program?<span class="plus">+</span></div>
    <div class="faq-item">Are you open on the Holidays?<span class="plus">+</span></div>
  </div>
  <div class="btn-row"><a class="btn" href="#">Contact Us</a></div>
</section>

<footer class="site-footer">
  <div class="footer-cols">
    <div class="footer-col" style="width:240px">
      <h4>Contact Us</h4>
      <div class="contact-line big"><svg width="14" height="14" viewBox="0 0 14 14"><path d="M3 1l2 3-1.5 1.5a8 8 0 0 0 5 5L10 9l3 2-1.5 2.5C6 13 1 8 .5 2.5z" fill="#0677BA"/></svg>404-555-0142</div>
      <div class="contact-line"><svg width="14" height="12" viewBox="0 0 14 12"><rect x="1" y="1" width="12" height="10" fill="none" stroke="#0677BA" stroke-width="1.4"/><path d="M1 1l6 5 6-5" fill="none" stroke="#0677BA" stroke-width="1.4"/></svg>hello@brightfold.example</div>
      <div class="contact-line"><svg width="12" height="14" viewBox="0 0 12 14"><path d="M6 0a5 5 0 0 0-5 5c0 4 5 9 5 9s5-5 5-9a5 5 0 0 0-5-5z" fill="#0677BA"/></svg>1420 Peachline Ave NE,<br>Atlanta, GA 30309</div>
    </div>
    <div class="footer-col" style="width:150px">
      <h4>Quick Links</h4>
      <ul><li>Home</li><li>About Us</li><li>Our Services</li><li>Why Choose Us</li><li>How To Get Started</li><li>FAQ</li><li>Contact</li></ul>
    </div>
    <div class="footer-col" style="width:220px">
      <h4>Our Services</h4>
      <ul><li>Commercial Services</li><li>Light Commercial Services</li><li>Professional Laundry Services</li><li>Pickup and Delivery</li><li>Wash and Fold</li><li>Press and Hang</li><li>Pricing</li></ul>
    </div>
    <div class="footer-col">
      <h4>Working Hours</h4>
      <ul><li class="hl">Monday - Friday: 7am - 7pm</li><li class="hl">Saturday: 8am - 5pm</li><li>Sunday: Closed</li><li>Holidays: 9am - 2pm</li></ul>
    </div>
  </div>
  <span class="to-top"><svg width="12" height="12" viewBox="0 0 12 12"><path d="M2 8l4-4 4 4" fill="none" stroke="#fff" stroke-width="2"/></svg></span>
  <div class="footer-bar">
    <span>© 2022 Brightfold Laundry Company. All rights reserved.</span>
    <span class="spacer"></span>
    <span>Terms and Conditions</span>
    <span>Privacy Notice</span>
  </div>
</footer>

</body>
</html>
```